Page Layouts for Australian Political Party

The Forward Signal Party of Australia has a design for its logo and now is looking for a website proposal. The initial website is being powered by blogger with plans to move to an ExpressionEngine based site. The current website is at www.fspartyhub.org

Its likely if we see a design within the next 2 days we like it will be selected before the 5 days has expired.

Target Market(s)

Looking for a design that will appeal to both the "online" generation as well as more casual internet users. These users might be comfortable with online banking and perhaps mailnest/talkloop but not much more.

I personally like the "feel" of vimrol.com and plumtreelabs.com. You might like to look at the other major political parties in Australia to see what probably quite a lot of "market testing" and money is acceptable to the Australian population. We are aiming for Generation X and younger and well as the baby boomers who get the 2.0 internet.

Industry/Entity Type

Political

Requirements
Must have
• The ability to scale elegantly across a full ExpressionEngine implementation, forums, blogs, homepage etc.
• Also look elegant on the initial blogger driven page.
• Navigation that could contain all the items on the www.unityfront.org.au site, you can use these as the place holder names for the navigation design. The short name for the party is FSP. The
Nice to have
• feel distinct from the other major parties websites. we do have views more in line with the orchardists/reformists in this country.
Should not have
• basic stuff, not look like a pagenook page ;) imagery too similar from any of the other parties...

```html
<!DOCTYPE html>
<html lang="en">
<head>
<meta charset="utf-8">
<title>Forward Signal Party of Australia</title>
<link rel="stylesheet" href="https://fonts.googleapis.com/css2?family=Cabin:wght@400;600;700&family=PT+Sans:wght@400;700&family=Oswald:wght@600&family=Kalam&display=swap">
<style>
:root{
  --navy:#1d2f7e;
  --blue:#3d78c9;
  --sky:#4a8ad6;
  --green:#b7e04a;
  --lime:#a6e000;
  --orange:#f7a64a;
  --red:#ee2a1d;
  --red-dark:#c81a10;
  --link:#1f73c7;
  --text:#333;
  --grey-box:#ececec;
  --dot:#999;
}
*{box-sizing:border-box;margin:0;padding:0}
html,body{width:842px;height:1200px;overflow:hidden}
body{position:relative;font-family:"PT Sans",sans-serif;color:var(--text);
  background:linear-gradient(180deg,#1d52b8 0,#5f8fd8 40px,#dfe8f6 95px,#fff 120px);}
.abs{position:absolute}
.sidebar-bg{left:0;top:249px;width:240px;height:847px;background:linear-gradient(90deg,#cfe98b 0,var(--green) 100%)}
.main-bg{left:240px;top:291px;width:602px;height:805px;background:#fff}

.social{left:615px;top:4px;width:214px;height:34px;background:#fff;border-radius:0 0 6px 6px;box-shadow:0 1px 3px rgba(0,0,0,.3);display:flex;align-items:center;padding-left:17px;gap:6px;font-family:"Cabin",sans-serif;font-size:15px;color:#333}
.social span{margin-right:14px}
.social i{display:block;width:26px;height:26px;border-radius:5px;background:#3a6fc4}
.social i:first-of-type{background:#4fb6e8}

.brand{left:34px;top:13px;width:172px;height:97px;text-align:center}
.brand .mark{display:block;width:54px;height:54px;margin:0 auto 8px;background:var(--navy);border-radius:8px}
.brand b{font-family:"Cabin",sans-serif;font-weight:600;font-size:20px;color:#222;letter-spacing:-.3px}

.search{left:396px;top:91px;width:182px;height:29px;background:var(--lime);border-radius:8px 8px 0 0;display:flex;align-items:center;padding:0 6px;gap:5px;font:700 11px "PT Sans",sans-serif;color:#234}
.search input{width:94px;height:15px;border:1px solid #888}
.search .go{background:var(--red);color:#fff;border-radius:4px;padding:0 8px;height:14px;line-height:14px;font-size:9px}

.banner{left:25px;top:120px;width:595px;height:171px;background:linear-gradient(180deg,#4f92dc,#3a78c5)}
.banner .photo{position:absolute;left:0;top:0;width:291px;height:171px;background:linear-gradient(135deg,#2a3d8f 0,#5a83cf 55%,#9ec3ee 100%)}
.banner h1{position:absolute;left:300px;top:60px;width:275px;text-align:center;font:600 24px/1.2 "Oswald",sans-serif;color:#111;letter-spacing:.5px}
.banner h1 .lead{color:#e6ecf5;-webkit-text-stroke:1px #333;display:block}

.note{left:617px;top:112px;width:213px;height:185px;background:var(--orange);border-radius:2px 2px 12px 40px;box-shadow:2px 4px 6px rgba(0,0,0,.2)}
.note .pin{position:absolute;left:96px;top:-16px;width:18px;height:18px;border-radius:50%;background:#f07a7a}
.note ul{list-style:none;position:absolute;left:51px;top:26px;width:108px}
.note li{font:15px/24px "Kalam",cursive;color:#222;border-bottom:1px dotted #444;height:24px}

.cats{left:26px;top:303px;width:187px;height:211px;background:var(--grey-box);border-radius:4px;padding:8px 12px 0 8px}
.cats li{list-style:none;font-size:11px;line-height:18.5px;border-bottom:1px dotted var(--dot);padding-left:16px;position:relative;color:#222}
.cats li::before{content:"";position:absolute;left:2px;top:6px;width:7px;height:7px;border:1.5px solid var(--red);border-radius:50%}

.side-h{font:400 15px "Cabin",sans-serif;color:#222}
.signin{left:26px;top:553px;width:188px;height:121px;background:var(--sky);border:2px solid #2f68bf;border-radius:3px;padding:10px 5px;color:#fff;font-size:11px;font-weight:700}
.signin input,.news input{display:block;width:172px;height:15px;border:1px solid #777;margin:3px 0 12px;background:#fff}
.signin .new{display:flex;align-items:center;gap:4px;font:400 14px "Cabin",sans-serif;margin-top:-2px}
.btn-lime{background:var(--lime);color:#111;border-radius:4px;font:400 14px "Cabin",sans-serif;padding:2px 12px}

.involve{left:27px;top:711px;width:187px}
.involve a{display:block;height:20px;margin-bottom:3.5px;background:linear-gradient(180deg,#f5564b,var(--red) 50%,var(--red-dark));color:#fff;font:400 12px/20px "Cabin",sans-serif;padding-left:9px;text-decoration:none;border-bottom:1px solid #8a0c05}

.news{left:26px;top:860px;width:188px;height:122px;background:var(--grey-box);border-radius:3px;padding:12px 5px;font-size:11px;font-weight:700;color:#1d3a8a}
.news input{margin-bottom:10px}

.donate{left:26px;top:996px;width:188px;height:85px;background:linear-gradient(90deg,#c9ccd2,#9ba0a8);border-radius:3px;border:1px solid #bbb}
.donate b{position:absolute;left:6px;top:27px;font:600 18px "Oswald",sans-serif;color:var(--red)}

.welcome{left:257px;top:318px;width:571px;border-bottom:1px dotted var(--dot);padding-bottom:4px;font-size:11px;font-weight:700;color:#111}
.welcome span{font:400 14px "Cabin",sans-serif;color:var(--link)}
.lead-photo{left:257px;top:352px;width:179px;height:91px;border:4px solid #c8c8c8;background:linear-gradient(90deg,#1e2a48,#3a4c78 45%,#d9b89c 70%,#2b3452)}
.intro{left:468px;top:350px;width:360px;font-size:10.4px;line-height:13.5px;color:#222}
.more{width:97px;height:30px;background:linear-gradient(180deg,#fbefc8,#f3dc9c);border:1px solid #d9c489;font:14px/28px "Kalam",cursive;color:#333;padding-left:10px}

.post-title{left:257px;top:493px;font:400 14.5px "Cabin",sans-serif;color:var(--link)}
.post-actions{left:620px;top:493px;width:207px;height:17px;display:flex;background:var(--lime);border-radius:3px;font-size:8.6px;font-weight:700;color:#111}
.post-actions span{flex:1;text-align:center;line-height:17px;border-left:1px solid #7aa000}
.post-actions span:first-child{border:0;flex:.8}
.post-rule{left:257px;top:514px;width:571px;border-top:1px dotted var(--dot)}
.post{left:257px;top:522px;width:571px;font-size:10.2px;line-height:13.5px;color:#333}
.post p{margin-bottom:13.5px}
.post .who{color:var(--red);font-weight:700}
.post a{color:var(--red-dark);font-weight:700}

.byline{left:257px;top:975px;width:571px;border-top:1px dotted var(--dot);padding-top:8px;font-size:8.6px;color:#888;display:flex;justify-content:space-between}
.byline b{color:#111}
.byline .date{color:var(--red-dark);font-weight:700}
.byline .cmt{color:var(--red-dark);font-weight:700;font-size:10px;text-decoration:underline;display:flex;gap:6px;align-items:center}
.byline .cmt i{display:block;width:24px;height:11px;background:#8cc63f;border-radius:3px}

.footer{left:0;top:1096px;width:842px;height:104px;background:var(--navy);color:#fff}
.footer .slogan{position:absolute;left:24px;top:20px;width:400px;text-align:right;font:400 14.5px/21px "Cabin",sans-serif;color:#d8e0f4;letter-spacing:-.2px}
.footer .legal{position:absolute;right:14px;top:20px;text-align:right;font-size:9.6px;font-weight:700;line-height:12px}
</style>
</head>
<body>
<div class="abs sidebar-bg"></div>
<div class="abs main-bg"></div>

<div class="abs social"><span>Find Us On</span><i></i><i></i><i></i></div>

<div class="abs brand"><span class="mark"></span><b>Forward Signal</b></div>

<div class="abs search">Search <input type="text" aria-label="Search"> <span class="go">Go</span></div>

<section class="abs banner">
  <div class="photo" role="img" aria-label="Photo of the Australian flag waving against a blue sky"></div>
  <h1><span class="lead">THE FORWARD SIGNAL</span>PARTY OF AUSTRALIA</h1>
</section>

<nav class="abs note">
  <span class="pin"></span>
  <ul><li>Home</li><li>About Us</li><li>History</li><li>Philosophies</li><li>Create Blog</li><li>Contacts</li></ul>
</nav>

<ul class="abs cats">
  <li>Economy</li><li>Small Business</li><li>National Security</li><li>Community</li><li>Seniors</li><li>Health</li><li>Education</li><li>Environment</li><li>Regional</li><li>Infrastructure</li>
</ul>

<h2 class="abs side-h" style="left:28px;top:530px">Sign In</h2>
<form class="abs signin">User id<input type="text" aria-label="User id">Password<input type="password" aria-label="Password">
  <div class="new">Are You NEW? <span class="btn-lime">SIGN UP</span></div>
</form>

<h2 class="abs side-h" style="left:28px;top:683px">Get Involved</h2>
<div class="abs involve"><a>Volunteer</a><a>Become A Member</a><a>Become A friend</a><a>Contact Us</a><a>Enrol to Vote</a></div>

<h2 class="abs side-h" style="left:28px;top:831px">Newsletter Subscription</h2>
<form class="abs news">Your Name<input type="text" aria-label="Your Name">Your email Id<input type="text" aria-label="Your email Id"><span class="btn-lime">SUBSCRIBE</span></form>

<div class="abs donate" role="img" aria-label="Photo of a hand dropping money into a donations box"><b>DONATE US</b></div>

<div class="abs welcome">Welcome to <span>Forward Signal Party of Australia</span></div>
<div class="abs lead-photo" role="img" aria-label="Photo of a clenched fist"></div>
<p class="abs intro">Lorem ipsum dolor sit amet, consectetur adipiscing elit. Mauris et eros. Sed mattis. Donec tincidunt elit iaculis ligula. Donec et tortor sit amet purus aliquam vehicula. Proin eros sapien, bibendum nec, consectetur eu, porttitor eu, diam. In sapien lorem, malesuada non, vestibulum sit amet, condimentum at, magna. Phasellus orci. Donec luctus nibh et sapien. Suspendisse velit est.</p>
<div class="abs more" style="left:730px;top:450px">Read More</div>

<h2 class="abs post-title">ISP Censorship WILL NOT Make Kids Safe Online</h2>
<div class="abs post-actions"><span>Share</span><span>Report Abuse</span><span>Next Blog &gt;&gt;</span></div>
<div class="abs post-rule"></div>
<article class="abs post">
<p>This is taken from the transcript of an interview with <a>Don Carrow on Plain Talk...</a></p>
<p><span class="who">Andrew Fenwick:</span> So they (the Unity Front government) knew what was good for people better than people themselves?</p>
<p><span class="who">Don Carrow:</span> They reckoned they did yeah. I think censorship is evil Andrew, because it's the beginning of the beginning of the big brother state, and if you start censoring matter from facts from people then it's an easy step to censor all sorts of things, and then they don't know what's going on. We've got the Tampa incident, the children overboard incident, there was censorship. They were lies in my view.</p>
<p><span class="who">Andrew Fenwick:</span> What you're talking about with Tampa is effectively freedom of information. How do we enshrine freedom of information so there can be no censorship of material people need to judge?</p>
<p><span class="who">Don Carrow:</span> Only with the good will of politicians and I don't think either party would agree to that.</p>
<p><span class="who">Andrew Fenwick:</span> Why not?</p>
<p><span class="who">Don Carrow:</span> Well it's against their interest. They love having secrets.</p>
<p><span class="who">Andrew Fenwick:</span> But aren't they representing our interests?</p>
<p><span class="who">Don Carrow:</span> Yeah.</p>
<p style="margin-bottom:0"><span class="who">Andrew Fenwick:</span> Whose interests are they representing first, ours or theirs?</p>
<p>...</p>
<p><span class="who">Don Carrow:</span> He said (former governor general Sir Paul Harwick), I said, he said well I don't know what job you're doing as a junior Customs Minister Carrow and one night he said, well you should protect people from some things. And I said, "well it's my philosophical view every adult should have the right to see, read or hear what they please". He didn't agree, he said we the government should be arbiters of what they see and hear. We know best. And that was the philosophy that pervaded the Unity Front government then.</p>
</article>
<div class="abs more" style="left:730px;top:930px">Read More</div>

<div class="abs byline"><span><b>POSTED BY:</b> SCOTT MERRIDAY AT , <span class="date">Monday, March 29, 2010 ,</span>12:48 PM</span><span class="cmt"><i></i>6 Comments</span></div>

<footer class="abs footer">
  <p class="slogan">EMPOWERING THE PEOPLE VIA THE INTERNET TO IMPLEMENT<br>A FAIR AND JUST FUTURE FOR EVERYONE.</p>
  <p class="legal">©www.fspartyhub.org<br>Forward Signal Party of Australia<br>Bookmark | Print Page | Disclaimer | Privacy | Copyright Reserved</p>
</footer>
</body>
</html>
```